tiny twirlers pre school dance classes

create a fun and eye catching flyer to encourage pre school children to attend pre school ballet & tap classes

www.tinytwirlers-demo.co.uk

Tuesday at the Oakbrook Leisure Centre Mellow Lane Surrey KX14 3QB

Friday Fenwick Lane Hall Ashwell Green KX18 2JD

contact 01632 960 418

email info@tinytwirlers-demo.co.uk

the flyer is a5 size please

```html
<!DOCTYPE html>
<html lang="en">
<head>
<meta charset="utf-8">
<title>Tiny Twirlers – Pre School Ballet and Tap Flyer</title>
<link rel="stylesheet" href="https://fonts.googleapis.com/css2?family=Mystery+Quest&display=swap">
<style>
  :root {
    --bg-light: #fde3ee;
    --bg-mid: #f9cfe1;
    --bg-deep: #f5b9d3;
    --brand-pink: #e4407f;
    --text-pink: #e3568a;
    --link-pink: #e0207a;
    --bubble-main: #f28fbe;
    --bubble-soft: #f6b4d2;
    --bubble-text: #fdecf3;
  }
  * { margin: 0; padding: 0; box-sizing: border-box; }
  html, body {
    width: 846px;
    height: 1200px;
    overflow: hidden;
    background: var(--bg-light);
  }
  .flyer {
    position: relative;
    width: 846px;
    height: 1200px;
    overflow: hidden;
    font-family: "Mystery Quest", cursive;
    color: var(--text-pink);
  }
  .flyer__backdrop {
    position: absolute;
    inset: 0;
    background:
      radial-gradient(circle at 15% 20%, var(--bg-deep) 0, transparent 28%),
      radial-gradient(circle at 85% 60%, var(--bg-deep) 0, transparent 26%),
      radial-gradient(circle at 30% 85%, var(--bg-mid) 0, transparent 30%),
      linear-gradient(180deg, var(--bg-mid), var(--bg-light) 50%, var(--bg-mid));
  }
  .brand {
    position: absolute;
    top: 88px;
    left: 0;
    width: 846px;
    text-align: center;
    font-size: 100px;
    font-weight: 400;
    line-height: 1;
    color: var(--brand-pink);
    white-space: nowrap;
  }
  .dancers {
    position: absolute;
    left: 84px;
    top: 298px;
    width: 312px;
    height: 300px;
    border-radius: 24px;
    background: linear-gradient(180deg, rgba(42,42,42,0.85), rgba(42,42,42,0.7));
  }
  .bubbles {
    position: absolute;
    left: 0;
    top: 0;
    width: 846px;
    height: 1200px;
  }
  .bubble-text {
    position: absolute;
    text-align: center;
    line-height: 1.2;
  }
  .bubble-text--classes {
    left: 462px;
    top: 330px;
    width: 264px;
    font-size: 34px;
    color: var(--bubble-text);
  }
  .bubble-text--signup {
    left: 661px;
    top: 468px;
    width: 160px;
    font-size: 30px;
    color: var(--brand-pink);
  }
  .info {
    position: absolute;
    left: 0;
    width: 846px;
    text-align: center;
    white-space: nowrap;
  }
  .info--web {
    top: 620px;
    font-size: 38px;
    line-height: 46px;
    color: var(--link-pink);
    font-weight: 700;
  }
  .venue {
    font-size: 34px;
    line-height: 59px;
  }
  .info--tuesday { top: 720px; }
  .info--friday { top: 882px; }
  .info--contact {
    top: 1060px;
    font-size: 28px;
    line-height: 52px;
  }
  .info--contact .phone { font-size: 46px; }
  .info--email {
    top: 1124px;
    font-size: 28px;
    line-height: 36px;
  }
</style>
</head>
<body>
  <main class="flyer">
    <div class="flyer__backdrop" role="img" aria-label="Soft pink background scattered with pale bokeh circles and pink sparkle stars"></div>

    <h1 class="brand">Tiny Twirlers</h1>

    <div class="dancers" role="img" aria-label="Five black silhouettes of little ballerinas in tutus, dancing in different poses"></div>

    <svg class="bubbles" width="846" height="1200" viewBox="0 0 846 1200" aria-hidden="true">
      <ellipse cx="594" cy="402" rx="132" ry="103" fill="var(--bubble-main)"/>
      <ellipse cx="741" cy="506" rx="84" ry="70" fill="var(--bubble-soft)"/>
    </svg>
    <p class="bubble-text bubble-text--classes">pre school<br>ballet and tap<br>classes!</p>
    <p class="bubble-text bubble-text--signup">sign up<br>now!</p>

    <p class="info info--web">www.tinytwirlers-demo.co.uk</p>

    <p class="info info--tuesday venue">Tuesday: at the Oakbrook Leisure Centre<br>Mellow Lane Surrey KX14 3QB</p>

    <p class="info info--friday venue">Friday: Fenwick Lane Hall<br>Ashwell Green KX18 2JD</p>

    <p class="info info--contact">contact: <span class="phone">01632 960 418</span></p>
    <p class="info info--email">email: info@tinytwirlers-demo.co.uk</p>
  </main>
</body>
</html>
```